The Hollow Lantern with Dov Ransbury

Create Podcast Art for Podwave. My podcast is about overcoming adversities.

Everyone's adversity is different and there's no one-size-fits-all solution, but when you hear someone's else's story of resilience and add a little salt to it, you can find the inspiration you need to write a new ending to your struggle.

Maybe you're going through something right now and you're afraid:

● You won't be successful
● People are talking behind your back
● You'll never get the help you need
● You're not a good husband or wife
● Your child is out of control and you'll never get through to him or her
● There isn't a light at the end of your tunnel
● You'll never get your finances out of the red
● Your spouse won't ever see things your way
● The world is never gonna change

Every story we tell on The Hollow Lantern podcast challenges those thoughts, because everyday people going through everyday stuff just like you show us otherwise.

This podcast is for you. And, it's different.

Most interviews I do, I try to go on location and interview in person.

You might not see us together on the screen,
but you'll sense the raw sincerity and closeness of a side-by-side interview through your speakers.

The colors I have chosen below are close to the website colors. If you need a better view of that go here http://www.dovransbury-example.com

I've attached two pictures for the podcast. I'm not sure which one to use just yet so I put them both here to see what i created by your great people!

Target Market(s)

People who are currently going through an Advesirty or have been through one. 28 - 40 age group.

Colors
ec1f27
ffffff
000000
fbee3e

Requirements
Must have
• Eye appeal and The title "The Hollow Lantern" with Dov Ransbury
• HAS to be stand-out, and it HAS to give a great first impression.
Nice to have
• The colors I have chosen are close to the website colors.

```html
<!DOCTYPE html>
<html lang="en">
<head>
<meta charset="utf-8">
<title>The Hollow Lantern with Dov Ransbury — Podcast Art</title>
<link rel="stylesheet" href="https://fonts.googleapis.com/css2?family=Teko:wght@500;600&family=Montserrat:wght@800&display=swap">
<style>
  :root {
    --brand-red: #ec1f27;
    --title-red: #f0141c;
    --brand-white: #ffffff;
    --brand-black: #000000;
    --brand-yellow: #fbee3e;
    --outline-grey: #9a9a9a;
    --shadow-red: #5a0a0c;
    --sky-blue: #5a95c4;
    --sky-deep: #2f6a99;
    --brick: #4a2420;
    --skin-lit: #b0652e;
    --skin-mid: #7a3e1e;
    --skin-shade: #3a1d10;
    --sweater-lit: #6b5a48;
    --sweater: #3a3129;
    --sweater-dark: #1d1915;
  }
  html, body {
    margin: 0;
    padding: 0;
    overflow: hidden;
    background: var(--brand-black);
  }
  .cover {
    position: relative;
    width: 1200px;
    height: 1200px;
    overflow: hidden;
    font-family: "Teko", sans-serif;
  }
  .cover-photo {
    position: absolute;
    inset: 0;
    background:
      /* sunlit shoulder of the sweater */
      radial-gradient(ellipse 520px 200px at 640px 800px, rgba(120,100,80,0.75) 0%, rgba(90,75,60,0.35) 50%, rgba(0,0,0,0) 100%),
      /* sweater mass across the lower half */
      linear-gradient(172deg, rgba(0,0,0,0) 0%, rgba(0,0,0,0) 56%, var(--sweater-lit) 62%, var(--sweater) 74%, var(--sweater-dark) 100%),
      /* warm lit head */
      radial-gradient(ellipse 330px 360px at 600px 360px, var(--skin-lit) 0%, var(--skin-mid) 48%, var(--skin-shade) 78%, rgba(58,29,16,0) 100%),
      /* warm neck and jaw */
      radial-gradient(ellipse 240px 200px at 720px 600px, rgba(122,62,30,0.95) 0%, rgba(58,29,16,0.6) 60%, rgba(0,0,0,0) 100%),
      /* sky and street on the right, brick wall on the left */
      linear-gradient(95deg, var(--brick) 0%, #3a1c1a 26%, #3d3430 40%, var(--sky-deep) 62%, var(--sky-blue) 100%);
  }
  .accent-stripes {
    position: absolute;
    top: 0;
    left: 101px;
    width: 64px;
    height: 1200px;
  }
  .title {
    position: absolute;
    left: 58px;
    top: 372px;
    margin: 0;
    font-weight: 600;
    font-size: 186px;
    line-height: 0.79;
    letter-spacing: 0;
    color: var(--title-red);
    -webkit-text-stroke: 5px var(--brand-white);
    paint-order: stroke fill;
    text-shadow: 4px 4px 0 var(--outline-grey), 8px 7px 0 var(--shadow-red);
    text-transform: uppercase;
  }
  .title span { display: block; }
  .host-with {
    position: absolute;
    left: 64px;
    top: 840px;
    font-family: "Montserrat", sans-serif;
    font-weight: 800;
    font-size: 32px;
    line-height: 1;
    color: var(--brand-yellow);
  }
  .host-name {
    position: absolute;
    left: 190px;
    top: 846px;
    display: flex;
    align-items: flex-start;
    gap: 14px;
    font-weight: 500;
    font-size: 96px;
    line-height: 0.82;
    color: var(--brand-red);
    text-transform: uppercase;
  }
  .host-name-lines span { display: block; }
  .host-mark {
    flex: none;
    width: 24px;
    height: 24px;
    margin-top: 16px;
    background: var(--brand-red);
  }
</style>
</head>
<body>
  <main class="cover">
    <div class="cover-photo" role="img" aria-label="Photo of the host in profile, looking out a sunlit window toward a blue sky and city street, wearing a dark knit sweater"></div>

    <svg class="accent-stripes" viewBox="0 0 64 1200" aria-hidden="true">
      <rect x="0" y="0" width="14" height="1200" fill="var(--brand-red)"/>
      <rect x="29" y="0" width="12" height="1200" fill="var(--brand-white)"/>
      <rect x="51" y="0" width="12" height="1200" fill="var(--brand-yellow)"/>
    </svg>

    <h1 class="title">
      <span>The</span>
      <span>Hollow</span>
      <span>Lantern</span>
    </h1>

    <span class="host-with">with</span>
    <div class="host-name">
      <span class="host-mark"></span>
      <span class="host-name-lines"><span>Dov</span><span>Ransbury</span></span>
    </div>
  </main>
</body>
</html>
```